Trifold Marketing Brochure for MBTH Larkfield

We want a colorful single sided trifold brochure (foldable single sheet of paper) for our cancer treatment center/infusion center/hematology oncology clinic in Edison, New Jersey (MBTH Larkfield). We want a motif that incorporates our company logo, but this doesn't need to be exclusive. We want eye catching, but modern and professional. Can incorporate the photos uploaded. Also need some blank areas for some descriptive text as well. Incorporate tel, fax, address and QR code on business card attached. Also mention names of Dr. Telmo Velstrom, Dr. Joren Velstrom, Dr. Gisel Thorne, and Dr. Mirela Velstrom as well.

Let's go for a 2 sided trifold brochure. No pictures of the physicians are necessary. Thank you!

Actually, can put smaller photos of the doctors and their names and degrees (MD). Also, we want to highlight the infusion area photo and the blue sky tiles (above the big chairs).. a blue sky theme as part of the overall motif would be great. Thank you!

```html
<!DOCTYPE html>
<html lang="en">
<head>
<meta charset="utf-8">
<title>MBTH Larkfield – Trifold Brochure, Inside Spread</title>
<link href="https://fonts.googleapis.com/css2?family=Poppins:ital,wght@0,400;0,500;0,600;0,700;1,400&display=swap" rel="stylesheet">
<style>
  :root {
    --sky: #14aedc;
    --sky-deep: #0f9cc8;
    --ink: #1c1c1f;
    --body: #3a3a40;
    --paper: #ffffff;
    --stage: #d4d5d9;
  }
  * { box-sizing: border-box; margin: 0; padding: 0; }
  html, body { width: 1200px; height: 800px; overflow: hidden; background: var(--stage); }
  body { font-family: "Poppins", sans-serif; color: var(--body); }

  .brochure {
    position: absolute; left: 30px; top: 30px;
    width: 1140px; height: 740px;
    display: flex; background: var(--paper);
    box-shadow: 0 10px 30px rgba(0,0,0,.18);
    overflow: hidden;
  }
  .panel { position: relative; width: 380px; height: 100%; }
  .panel--services { background: linear-gradient(90deg, #f4f5f7 0%, #ffffff 45%, #f1f2f5 100%); }
  .panel--team { background: linear-gradient(90deg, #eceef1 0%, #f6f7f9 60%, #ffffff 100%); }

  .sky-band {
    position: absolute; left: 0; right: 0; bottom: 0; height: 168px; z-index: 1;
    background: linear-gradient(90deg, var(--sky) 0 380px, var(--sky-deep) 380px 760px, var(--sky) 760px 100%);
  }

  /* Panel 1: photo stack */
  .photo-stack { position: absolute; left: 34px; top: 34px; width: 312px; display: flex; flex-direction: column; gap: 8px; }
  .photo { height: 162px; }
  .photo--consult { background: linear-gradient(135deg, #e9e4df 0%, #c9c2bb 55%, #8d8680 100%); }
  .photo--ward { background: linear-gradient(160deg, #f3f4f6 0%, #c5c7cb 55%, #7b7d82 100%); }
  .photo--infusion { background: linear-gradient(170deg, #9fd7f0 0%, #d9dbdf 35%, #a9abb0 70%, #6d6f74 100%); }

  .brand {
    position: absolute; left: 34px; bottom: 94px; z-index: 2;
    display: flex; align-items: center; gap: 8px;
    color: #fff; font-weight: 600; font-size: 19px; letter-spacing: .5px;
  }
  .brand__dot { width: 12px; height: 12px; border-radius: 50%; background: #fff; }
  .brand-divider { position: absolute; left: 222px; bottom: 30px; width: 1px; height: 112px; background: rgba(255,255,255,.85); z-index: 2; }

  .about {
    position: absolute; left: 240px; bottom: 26px; width: 480px; z-index: 2;
    color: #fff; font-size: 10.5px; line-height: 1.6;
  }

  /* Panel 2: services */
  .section-title { font-weight: 700; color: var(--ink); font-size: 21px; letter-spacing: .2px; }
  .panel--services .section-title { position: absolute; left: 36px; top: 40px; }
  .services { position: absolute; left: 36px; top: 86px; width: 316px; list-style: none; display: flex; flex-direction: column; gap: 10px; }
  .service { display: flex; gap: 8px; font-size: 11px; line-height: 1.5; }
  .service__tick { flex: none; width: 12px; height: 12px; margin-top: 3px; }
  .service__name { color: var(--sky); font-weight: 600; }

  /* Panel 3: specialists */
  .panel--team .section-title { position: absolute; left: 30px; top: 40px; }
  .team-intro { position: absolute; left: 30px; top: 76px; width: 322px; font-size: 11px; line-height: 1.5; color: var(--ink); font-weight: 500; }
  .doctors { position: absolute; left: 30px; top: 156px; width: 322px; list-style: none; display: flex; flex-direction: column; gap: 12px; }
  .doctor { display: flex; gap: 12px; align-items: flex-start; }
  .doctor__photo { flex: none; width: 70px; height: 74px; background: linear-gradient(160deg, #f2f2f2 0%, #c8c8cc 100%); }
  .doctor__name { color: var(--sky); font-weight: 600; font-size: 12px; margin-bottom: 2px; }
  .doctor__bio { font-size: 9px; line-height: 1.45; }
</style>
</head>
<body>
<main class="brochure">

  <section class="panel panel--gallery">
    <div class="photo-stack">
      <div class="photo photo--consult" role="img" aria-label="Photo of a clinician with a patient at an examination device"></div>
      <div class="photo photo--ward" role="img" aria-label="Photo of a bright clinic treatment room with yellow chairs"></div>
      <div class="photo photo--infusion" role="img" aria-label="Photo of the infusion area with recliner chairs under blue sky ceiling tiles"></div>
    </div>
  </section>

  <section class="panel panel--services">
    <h2 class="section-title">Our Services</h2>
    <ul class="services">
      <li class="service"><svg class="service__tick" viewBox="0 0 12 12"><circle cx="6" cy="6" r="6" fill="#14aedc"/><path d="M3.2 6.2l1.9 1.8 3.7-3.8" fill="none" stroke="#fff" stroke-width="1.4"/></svg><p><span class="service__name">Oncology Care:</span> Diagnosis and customized treatment plans for all types of cancers, including but not limited to breast, lung, prostate, and colon cancers.</p></li>
      <li class="service"><svg class="service__tick" viewBox="0 0 12 12"><circle cx="6" cy="6" r="6" fill="#14aedc"/><path d="M3.2 6.2l1.9 1.8 3.7-3.8" fill="none" stroke="#fff" stroke-width="1.4"/></svg><p><span class="service__name">Hematology Care:</span> Expert diagnosis and management of blood disorders, such as anemia, bleeding/clotting disorders, and blood cancers like leukemia and lymphoma.</p></li>
      <li class="service"><svg class="service__tick" viewBox="0 0 12 12"><circle cx="6" cy="6" r="6" fill="#14aedc"/><path d="M3.2 6.2l1.9 1.8 3.7-3.8" fill="none" stroke="#fff" stroke-width="1.4"/></svg><p><span class="service__name">Infusion Therapy:</span> Administration of medications, fluids, or nutrition directly into the body through intravenous, subcutaneous, or intrathecal routes.</p></li>
      <li class="service"><svg class="service__tick" viewBox="0 0 12 12"><circle cx="6" cy="6" r="6" fill="#14aedc"/><path d="M3.2 6.2l1.9 1.8 3.7-3.8" fill="none" stroke="#fff" stroke-width="1.4"/></svg><p><span class="service__name">Chemotherapy:</span> Use of anti-cancer drugs tailored to patient's cancer type and treatment goals, given alone or in combination with other therapies.</p></li>
      <li class="service"><svg class="service__tick" viewBox="0 0 12 12"><circle cx="6" cy="6" r="6" fill="#14aedc"/><path d="M3.2 6.2l1.9 1.8 3.7-3.8" fill="none" stroke="#fff" stroke-width="1.4"/></svg><p><span class="service__name">Targeted Therapy:</span> Anti-cancer treatments like immunotherapy and small molecule drugs that specifically attack cancer cells while reducing damage to healthy cells.</p></li>
      <li class="service"><svg class="service__tick" viewBox="0 0 12 12"><circle cx="6" cy="6" r="6" fill="#14aedc"/><path d="M3.2 6.2l1.9 1.8 3.7-3.8" fill="none" stroke="#fff" stroke-width="1.4"/></svg><p><span class="service__name">Radiation Therapy:</span> Use of high energy X-rays targeted at cancer cells to damage their DNA, stop growth and eliminate them. We provide external beam radiation as well as radioactive seed implantation.</p></li>
    </ul>
  </section>

  <section class="panel panel--team">
    <h2 class="section-title">Meet Our Specialists</h2>
    <p class="team-intro">Our team of compassionate doctors brings decades of cancer care experience. Each specialist provides customized treatment plans focused on the latest research and personalized patient care.</p>
    <ul class="doctors">
      <li class="doctor"><div class="doctor__photo" role="img" aria-label="Portrait photo of Dr. Gisel Thorne"></div><div><h3 class="doctor__name">Gisel Thorne, MD</h3><p class="doctor__bio">Dr. Gisel Thorne is an oncology and hematology specialist practicing in Larkfield, NJ. She received her medical degree from Corvale Medical College and has been in practice for more than 25 years.</p></div></li>
      <li class="doctor"><div class="doctor__photo" role="img" aria-label="Portrait photo of Dr. Joren Velstrom"></div><div><h3 class="doctor__name">Joren Velstrom, MD</h3><p class="doctor__bio">With more than 25 years of experience in the medical field, Dr. Joren Velstrom is in private practice in Larkfield, NJ and board certified in Internal Medicine as well as Medical Oncology.</p></div></li>
      <li class="doctor"><div class="doctor__photo" role="img" aria-label="Portrait photo of Dr. Telmo Velstrom"></div><div><h3 class="doctor__name">Telmo Velstrom, MD</h3><p class="doctor__bio">Dr. Telmo Velstrom has extensive experience in the field of hematology and oncology. He is presently the chairman of the Division of Hematology/Oncology at Halvern University Hospital, Brookmere, NJ.</p></div></li>
      <li class="doctor"><div class="doctor__photo" role="img" aria-label="Portrait photo of Dr. Mirela Velstrom"></div><div><h3 class="doctor__name">Mirela Velstrom, MD</h3><p class="doctor__bio">Dr. Mirela Velstrom has over 30 years experience in oncology and hematology. She completed trainings in India, New Jersey and New York, earning board certifications in Internal Medicine and Medical Oncology.</p></div></li>
    </ul>
  </section>

  <div class="sky-band"></div>
  <div class="brand"><span class="brand__dot"></span>MBTH Larkfield</div>
  <div class="brand-divider"></div>
  <p class="about">Meridian Blood &amp; Tumor Health of Larkfield, NJ is staffed by expert hematologists and oncologists. These experienced physicians are fully dedicated to our mission of providing patient-centered care, utilizing the latest technology to treat a range of hematologic conditions and perform oncology procedures, as well as perform geriatric-related health procedures. We also conduct clinical trials for new and developing treatments and procedures, the better to expand our understanding of cancer and our capacity to treat it. Get in touch with Meridian Blood &amp; Tumor Health at 42 Orchard Lane, Suite 3, Larkfield NJ 08990 today.</p>

</main>
</body>
</html>
```